Hydrographic business needs a business card that reaches hunters and off-road enthusiasts

We need a business card for a new hydrographics company catering to customers such as hunters, off-road ATV riders and custom vehicle enthusiasts. A western theme is preferred but professional. Our service should be thought of as upper end graphic design on firearms, off road vehicles, motorcycles, etc... See www.caldorfx.com for ideas on patterns, colors, etc...

Target Market(s)

Hunters, off road enthusiasts, custom car enthusiasts, motorcycle riders...

Industry/Entity Type

Graphic Design

```html
<!DOCTYPE html>
<html lang="en">
<head>
<meta charset="utf-8">
<title>Caldor FX – Business Card</title>
<link href="https://fonts.googleapis.com/css2?family=Arvo:wght@400;700&display=swap" rel="stylesheet">
<style>
  :root {
    --backdrop: #2a2a2a;
    --frame-red: #8c1a1d;
    --frame-red-dark: #6e1215;
    --wood-light: #e6bd80;
    --wood-mid: #d9a766;
    --wood-dark: #c58f52;
    --ink: #141210;
    --logo-red: #8c1a1d;
  }
  * { box-sizing: border-box; margin: 0; padding: 0; }
  html, body {
    width: 1200px; height: 799px; overflow: hidden;
    background: var(--backdrop);
  }
  .canvas {
    position: relative; width: 1200px; height: 799px;
    display: flex; align-items: center; justify-content: center;
  }
  .card {
    position: relative; width: 900px; height: 514px;
    background: var(--frame-red);
    font-family: "Arvo", Georgia, serif;
    color: var(--ink);
  }
  .card__wood {
    position: absolute; inset: 26px;
    background: linear-gradient(100deg, var(--wood-light) 0%, var(--wood-mid) 45%, var(--wood-light) 70%, var(--wood-dark) 100%);
    box-shadow: inset 0 0 0 2px var(--frame-red-dark);
  }
  .card__notch {
    position: absolute; width: 56px; height: 56px; border-radius: 50%;
    background: var(--frame-red);
  }
  .card__notch--tl { left: -2px; top: -2px; }
  .card__notch--tr { right: -2px; top: -2px; }
  .card__notch--bl { left: -2px; bottom: -2px; }
  .card__notch--br { right: -2px; bottom: -2px; }

  .brand {
    position: absolute; left: 70px; top: 80px; width: 240px;
    display: flex; flex-direction: column; align-items: center; gap: 18px;
  }
  .brand__dot {
    width: 130px; height: 130px; border-radius: 50%;
    border: 14px solid var(--logo-red);
  }
  .brand__name {
    font-weight: 700; font-size: 34px; letter-spacing: 4px;
    color: var(--logo-red); text-transform: uppercase;
  }

  .person {
    position: absolute; left: 390px; top: 120px;
  }
  .person__name {
    display: inline-block; font-weight: 700; font-size: 40px;
    border-bottom: 4px solid var(--ink); padding-bottom: 2px;
    box-shadow: 0 5px 0 -2px transparent, 0 8px 0 -6px var(--ink);
  }
  .contacts { list-style: none; margin-top: 26px; }
  .contacts__item {
    display: flex; align-items: center; gap: 18px;
    font-size: 25px; height: 48px;
  }
  .contacts__icon { width: 34px; height: 30px; flex: none; }
  .contacts__item--plain { padding-left: 52px; }

  .address {
    position: absolute; left: 150px; bottom: 50px;
    font-size: 21px; letter-spacing: 0.5px;
  }
</style>
</head>
<body>
<main class="canvas">
  <article class="card">
    <div class="card__wood" role="img" aria-label="Light pine wood grain panel">
      <span class="card__notch card__notch--tl"></span>
      <span class="card__notch card__notch--tr"></span>
      <span class="card__notch card__notch--bl"></span>
      <span class="card__notch card__notch--br"></span>
    </div>

    <div class="brand">
      <span class="brand__dot"></span>
      <span class="brand__name">Caldor FX</span>
    </div>

    <section class="person">
      <h1 class="person__name">Wade Caldor</h1>
      <ul class="contacts">
        <li class="contacts__item">
          <svg class="contacts__icon" viewBox="0 0 34 30" aria-hidden="true">
            <path d="M3 10 Q17 0 31 10 L28 14 L23 12 L23 9 Q17 7 11 9 L11 12 L6 14 Z" fill="#141210"/>
            <path d="M9 14 L25 14 L30 27 L4 27 Z" fill="#141210"/>
            <circle cx="17" cy="20" r="3.5" fill="#d9a766"/>
          </svg>
          <span>214-555-0187</span>
        </li>
        <li class="contacts__item">
          <svg class="contacts__icon" viewBox="0 0 34 30" aria-hidden="true">
            <rect x="2" y="5" width="30" height="20" fill="#141210"/>
            <path d="M3 6 L17 17 L31 6" fill="none" stroke="#d9a766" stroke-width="2"/>
          </svg>
          <span>wade@caldorfx.com</span>
        </li>
        <li class="contacts__item">
          <svg class="contacts__icon" viewBox="0 0 34 30" aria-hidden="true">
            <g fill="none" stroke="#141210" stroke-width="2">
              <circle cx="13" cy="13" r="10"/>
              <ellipse cx="13" cy="13" rx="4.5" ry="10"/>
              <path d="M3 13 H23 M5 7 H21 M5 19 H21"/>
              <circle cx="23" cy="21" r="4.5" fill="#d9a766"/>
              <path d="M26.5 24.5 L32 29" stroke-width="3"/>
            </g>
          </svg>
          <span>www.caldorfx.com</span>
        </li>
        <li class="contacts__item contacts__item--plain">
          <span>www.caldorfx.com</span>
        </li>
      </ul>
    </section>

    <p class="address">112 Ridge County Road 2040 Cedar Bluff, TX 75000</p>
  </article>
</main>
</body>
</html>
```